Brochure Design Project

I am looking for a trifold brochure.
I would like it to be square (5.5 x 5.5)
The back needs to be reserved for a map and logo information.

we are a financial planning firm. we have been in operation for 15 years.
our clients are ecstatic and continue to refer others to us.

Brochure COPY:
Building Wealth, Building Futures
We start with your goals. Then we build a comprehensive strategy to manage your investments, grow your wealth, minimize your tax burden and protect your family. Most importantly, we keep you informed about market change, opportunities and concerns before they impact you, so you can make confident decisions about your future, every step of the way.

Understanding and Expertise (bios)
Steadfast Money Partners is led by Lorna Feldskov and Miriam Oakhurst, experienced business partners who take the time to listen to you, understand your needs and present you with all your options.
Our focus in on your future, and building a confident and financially secure path for you and your family for the years ahead.

Lorna Feldskov, BSc, MBA, CPA, CA, CFP, FMA, CPCA
Certified Financial Planner

With years of experience in tax, investment, estate and retirement issues - and an extensive business background - Lorna provided her clients with important financial insights and clear direction in a friendly and open manner.

Miriam Oakhurst, BSEd, FMA, CPCA, CFP, FCSI, CIM

After a successful tennis career Miriam joined Lorna in the financial industry. Miriam quickly discovered how much she enjoys working with people and helping them to achieve their goals. Leveraging the discipline and work ethic developed during her tennis career, Miriam has been instrumental in creating the successful process used by Steadfast Money Partners.

People Trust Us to Help Them
The important things in life are often neglected due to the demands of day to day, including financial planning and wealth management. But it doesn't have to be that way when you have a trustworthy team looking out for you.
At Steadfast Money Partners we have the knowledge, experience and resources to help you move forward and realize your financial goals.

(side note) on the back of the brochure it should have the SMP logo, the office address, 382 Kettlewood Rd. E. Mississauga, ON L5R 7M4, and our website address.

Reason: Am juggling a number of different projects so need to extend the deadline on this one. Will provide copy for the project by end of day today.

Target Market(s)

We would like the brochure to appeal to the high net worth client who is currently working with an advisor but is not getting the attention from them.

Industry/Entity Type

Financial

Requirements
Must have
• SMP Logo on the front. The logo is blue with black font and has a tagline with it that says "Choose your path, change your future."
you can see the logo at www.plantharvestsoon.ca

One page must be about the two advisors, Lorna Feldskov and Miriam Oakhurst.
(leave an open area for bios and we will fill it in)

We want it to talk about building wealth and passing it on to the next generation.
Should not have
• Financial lingo.

```html
<!DOCTYPE html>
<html lang="en">
<head>
<meta charset="utf-8">
<title>Steadfast Money Partners – Trifold Brochure</title>
<link href="https://fonts.googleapis.com/css2?family=Arimo:ital,wght@0,400;0,700;1,700&family=Roboto+Condensed:wght@400;700&display=swap" rel="stylesheet">
<style>
  :root {
    --stage: #c8a57a;
    --navy: #123a72;
    --navy-deep: #0b2a57;
    --blue: #1d55a0;
    --blue-light: #3c78c2;
    --white: #ffffff;
    --mist: #e4ecf5;
    --cream: #fff4e0;
    --orange: #f07a1a;
    --red: #e0351f;
    --ink: #1c2f52;
  }
  * { box-sizing: border-box; margin: 0; padding: 0; }
  html, body { width: 1200px; height: 1200px; overflow: hidden; }
  body {
    background: var(--stage);
    font-family: "Arimo", Arial, sans-serif;
    position: relative;
  }

  /* ---------- Front cover ---------- */
  .cover {
    position: absolute; left: 40px; top: 220px;
    width: 300px; height: 760px;
    background: var(--white);
    overflow: hidden;
    box-shadow: 0 6px 18px rgba(0,0,0,.25);
  }
  .cover__bg { position: absolute; inset: 0; }
  .cover__title {
    position: absolute; right: 18px; top: 78px;
    font-family: "Roboto Condensed", Arial, sans-serif;
    font-size: 21px; color: var(--navy); letter-spacing: .2px;
  }
  .cover__logo {
    position: absolute; left: 20px; top: 290px;
    width: 130px; height: 64px;
    background: var(--white); border: 2px solid var(--mist);
    display: flex; align-items: center; gap: 6px; padding: 6px 8px;
  }
  .logo-mark { width: 12px; height: 12px; background: var(--blue); flex: none; }
  .logo-name { font-size: 11px; font-weight: 700; color: var(--navy); line-height: 1.2; }
  .cover__address {
    position: absolute; left: 34px; top: 378px;
    width: 96px; padding: 6px;
    background: var(--white);
    font-size: 8px; line-height: 1.35; color: var(--ink);
  }
  .cover__services {
    position: absolute; right: 16px; top: 450px;
    list-style: none; text-align: right;
  }
  .cover__services li {
    font-weight: 700; font-style: italic; font-size: 15px;
    color: var(--white); margin-bottom: 16px; letter-spacing: .3px;
  }
  .cover__web {
    position: absolute; left: 18px; top: 676px;
    font-size: 11px; color: var(--red); letter-spacing: .3px;
  }
  .cover__footer-logo {
    position: absolute; right: 18px; bottom: 22px;
    display: flex; align-items: center; gap: 5px;
  }
  .cover__footer-logo .logo-name { font-size: 9px; }
  .cover__footer-logo .logo-mark { width: 9px; height: 9px; }

  /* ---------- Inside spread ---------- */
  .spread {
    position: absolute; left: 380px; top: 220px;
    width: 780px; height: 760px;
    overflow: hidden;
    box-shadow: 0 6px 18px rgba(0,0,0,.25);
  }
  .spread__bg { position: absolute; inset: 0; }
  .panel { position: absolute; top: 0; width: 260px; height: 760px; }
  .panel--left { left: 0; }
  .panel--middle { left: 260px; }
  .panel--right { left: 520px; }

  .photo {
    position: absolute;
    border: 3px solid var(--white);
    background: linear-gradient(135deg, #d9b48c, #8a6a4e 55%, #c9d6e6);
  }
  .photo--cool { background: linear-gradient(135deg, #c7d3e0, #7d8fa5 55%, #e8dccb); }
  .photo--sky { background: linear-gradient(180deg, #bcd6ee, #e9c9a5); }
  .portrait {
    position: absolute; width: 82px; height: 82px;
    transform: rotate(10deg);
    border: 3px solid var(--blue-light);
    background: linear-gradient(135deg, #5c93d2, #c9a48a 60%, #2f5f9e);
  }

  .callout {
    position: absolute;
    background: var(--cream);
    border: 2px solid var(--orange);
    border-radius: 10px;
    padding: 10px 12px;
  }
  .callout__heading {
    font-size: 12px; font-weight: 700; color: var(--red); margin-bottom: 5px;
  }
  .callout p { font-size: 9.5px; line-height: 1.35; color: var(--ink); margin-bottom: 4px; }

  .bio { position: absolute; color: var(--white); }
  .bio__name { font-size: 9.5px; font-weight: 700; line-height: 1.3; }
  .bio__role { font-size: 9.5px; margin-bottom: 5px; }
  .bio p { font-size: 9.5px; line-height: 1.38; }

  /* Miriam's text follows the diagonal rule on its left edge */
  .bio--wrapped { width: 238px; }
  .bio__rule-space {
    float: left;
    width: 178px; height: 270px;
    shape-outside: polygon(0 0, 178px 0, 43px 270px, 0 270px);
  }
</style>
</head>
<body>

<!-- Front cover -->
<section class="cover" aria-label="Brochure front cover">
  <svg class="cover__bg" width="300" height="760" viewBox="0 0 300 760" aria-hidden="true">
    <defs>
      <linearGradient id="coverBlue" x1="0" y1="0" x2="0" y2="1">
        <stop offset="0" stop-color="#2a63ad"/>
        <stop offset="1" stop-color="#123a72"/>
      </linearGradient>
    </defs>
    <path d="M0 170 C 90 150, 200 190, 300 230 L300 650 L0 650 Z" fill="url(#coverBlue)"/>
    <path d="M0 170 C 90 150, 200 190, 300 230 L300 245 C 200 210, 90 172, 0 190 Z" fill="#5a8fd0" opacity=".6"/>
    <path d="M150 250 C 190 210, 240 180, 300 160" stroke="#ffffff" stroke-width="4" fill="none"/>
    <path d="M0 600 C 100 640, 200 610, 300 590 L300 650 L0 650 Z" fill="#0b2a57"/>
  </svg>
  <h1 class="cover__title">Steadfast Money Partners</h1>
  <div class="cover__logo">
    <span class="logo-mark"></span>
    <span class="logo-name">Steadfast Money Partners</span>
  </div>
  <address class="cover__address">382 Kettlewood Rd. E.<br>Mississauga, ON<br>L5R 7M4</address>
  <ul class="cover__services">
    <li>Financial Planning</li>
    <li>Wills &amp; Estate Planning</li>
    <li>Insurance</li>
    <li>Tax Planning</li>
  </ul>
  <div class="cover__web">www.plantharvestsoon.ca</div>
  <div class="cover__footer-logo">
    <span class="logo-mark"></span>
    <span class="logo-name">Steadfast Money Partners</span>
  </div>
</section>

<!-- Inside spread -->
<section class="spread" aria-label="Brochure inside spread">
  <svg class="spread__bg" width="780" height="760" viewBox="0 0 780 760" aria-hidden="true">
    <defs>
      <linearGradient id="spreadBlue" x1="0" y1="0" x2="1" y2="1">
        <stop offset="0" stop-color="#1d55a0"/>
        <stop offset=".55" stop-color="#123a72"/>
        <stop offset="1" stop-color="#0b2a57"/>
      </linearGradient>
    </defs>
    <rect width="780" height="760" fill="url(#spreadBlue)"/>
    <line x1="260" y1="0" x2="260" y2="760" stroke="#0b2a57" stroke-width="1"/>
    <line x1="520" y1="0" x2="520" y2="760" stroke="#0b2a57" stroke-width="1"/>
    <line x1="495" y1="240" x2="310" y2="610" stroke="#ffffff" stroke-width="1.5" opacity=".8"/>
    <path d="M0 680 C 200 650, 520 730, 780 670 L780 760 L0 760 Z" fill="#e4ecf5"/>
    <path d="M0 690 C 220 662, 520 740, 780 682" stroke="#3c78c2" stroke-width="3" fill="none"/>
    <path d="M0 708 C 240 685, 520 752, 780 702" stroke="#ffffff" stroke-width="2" fill="none"/>
  </svg>

  <!-- Left panel -->
  <div class="panel panel--left">
    <div class="photo" style="left:30px; top:40px; width:112px; height:82px;" role="img" aria-label="Photo of a smiling multi-generation family"></div>
    <div class="callout" style="left:12px; top:150px; width:236px;">
      <h2 class="callout__heading">Building Wealth, Building Futures</h2>
      <p>We start with your goals. Then we build a comprehensive strategy to manage your investments, grow your wealth, minimize your tax burden and protect your family. Most importantly, we keep you informed about market change, opportunities and concerns before they impact you, so you can make confident decisions about your future, every step of the way.</p>
    </div>
    <div class="photo photo--cool" style="left:30px; top:375px; width:112px; height:82px;" role="img" aria-label="Photo of advisors meeting with a couple"></div>
    <div class="callout" style="left:12px; top:478px; width:236px;">
      <h2 class="callout__heading">Understanding and Expertise</h2>
      <p>Steadfast Money Partners is led by Lorna Feldskov and Miriam Oakhurst, experienced business partners who take the time to listen to you, understand your needs and present you with all your options.</p>
      <p>Our focus is on your future, and building a confident and financially secure path for you and your family for the years ahead.</p>
    </div>
  </div>

  <!-- Middle panel -->
  <div class="panel panel--middle">
    <div class="portrait" style="left:80px; top:14px;" role="img" aria-label="Portrait of Lorna Feldskov"></div>
    <div class="bio" style="left:22px; top:112px; width:220px;">
      <div class="bio__name">Lorna Feldskov, BSc, MBA, CPA, CA, CFP, FMA, CPCA</div>
      <div class="bio__role">Certified Financial Planner</div>
      <p>With years of experience in tax, investment, estate and retirement issues - and an extensive business background - Lorna provided her clients with important financial insights and clear direction in a friendly and open manner.</p>
    </div>
    <div class="bio bio--wrapped" style="left:12px; top:340px;">
      <div class="bio__rule-space" aria-hidden="true"></div>
      <p>After a successful tennis career Miriam joined Lorna in the financial industry. Miriam quickly discovered how much she enjoys working with people and helping them to achieve their goals. Leveraging the discipline and work ethic developed during her tennis career, Miriam has been instrumental in creating the successful process used by Steadfast Money Partners.</p>
    </div>
    <div class="bio" style="left:22px; top:618px; width:200px;">
      <div class="bio__name">Miriam Oakhurst, BSEd, FMA, CPCA, CFP, FCSI, CIM</div>
    </div>
    <div class="portrait" style="left:160px; top:652px;" role="img" aria-label="Portrait of Miriam Oakhurst"></div>
  </div>

  <!-- Right panel -->
  <div class="panel panel--right">
    <div class="photo photo--cool" style="left:120px; top:150px; width:112px; height:82px;" role="img" aria-label="Photo of a couple reviewing plans at home"></div>
    <div class="callout" style="left:12px; top:250px; width:236px;">
      <h2 class="callout__heading">People Trust Us to Help Them</h2>
      <p>The important things in life are often neglected due to the demands of day to day, including financial planning and wealth management. But it doesn't have to be that way when you have a trustworthy team looking out for you.</p>
      <p>At Steadfast Money Partners we have the knowledge, experience and resources to help you move forward and realize your financial goals.</p>
    </div>
    <div class="photo photo--sky" style="left:120px; top:500px; width:112px; height:82px;" role="img" aria-label="Photo of raised hands celebrating against the sky"></div>
  </div>
</section>

</body>
</html>
```